Capability statement for an Electrical Business based in Sydney Australia

The aim for the Capability statement is for us to look more professional when we meet someone or after cold calling and have to send them our business details.
Need something simple, efficient and to the point.

It should have the following content
- Our mission (details can be as attached PDF)
- Areas we service (this can be a google map of areas we service but basically the areas are
Metro Sydney with our work centralised around the Norwest, Hills, Inner west and Epping area)
- List of services we provide (as PDF)
- Details about us; who we are, contact details, licenses (as PDF)
- Why they should choose us
(As pdf)

Right now, we're just after a nice format we're happy with, the details we are happy to provide with once we have a design in mind.

I've attached our current existing capability statement and what our details are. Also, our website is
https://brightwirepro.com.au/

Thanks in advance!

Requirements
Should not have
• Should not be complicated for the reader

```html
<!DOCTYPE html>
<html lang="en">
<head>
<meta charset="utf-8">
<title>BrightWire Pro – Capability Statement</title>
<link rel="stylesheet" href="https://fonts.googleapis.com/css2?family=Montserrat:wght@300;400;600;700;800&display=swap">
<style>
:root{
  --red:#e1302a;
  --black:#121212;
  --ink:#1d1d1d;
  --grey:#5e5e5e;
  --rule:#c9c9c9;
  --paper:#ffffff;
  --bg:#e9e7e5;
}
*{margin:0;padding:0;box-sizing:border-box}
html,body{width:1200px;height:418px;overflow:hidden;background:var(--bg);font-family:"Montserrat",sans-serif}
.sheet{position:absolute;top:9px;width:282px;height:400px;background:var(--paper);overflow:hidden}
.sheet--front{left:298px}
.sheet--back{left:620px}

.mission{position:absolute;left:0;top:8px;width:115px;height:56px;background:var(--red);color:#fff;
  font-weight:700;font-size:5.4px;letter-spacing:.55px;line-height:1.32;text-align:center;
  display:flex;align-items:center;justify-content:center;padding:0 8px}
.brand{position:absolute;left:128px;top:13px;width:146px;color:var(--red);font-weight:800;line-height:1}
.brand__name{font-size:19.5px;letter-spacing:.3px}
.brand__sub{font-size:14px;letter-spacing:17px;margin-top:4px;padding-left:2px}

.photo-grid{position:absolute;left:0;top:64px;width:282px;height:110px;display:grid;grid-template-columns:repeat(4,1fr);grid-template-rows:1fr 1fr;gap:1px;background:#222}
.photo-grid div{width:100%;height:100%}
.ph-house{background:linear-gradient(160deg,#2c4468,#6f6a5c 70%,#3b3a2f)}
.ph-kitchen-dark{background:linear-gradient(150deg,#4b535a,#2b2f33)}
.ph-kitchen-grey{background:linear-gradient(160deg,#5f6669,#303437)}
.ph-kitchen-warm{background:linear-gradient(150deg,#8a7d6a,#3b342c)}
.ph-kitchen-white{background:linear-gradient(160deg,#e4e2dd,#a9a59d)}
.ph-kitchen-bright{background:linear-gradient(150deg,#d8d4cb,#8d8a84)}
.ph-garden{background:linear-gradient(160deg,#3d4a2a,#1d2414)}
.ph-living{background:linear-gradient(150deg,#a57c48,#4e3a22)}

.title-band{position:absolute;left:0;top:174px;width:282px;height:21px;background:var(--black);color:#fff;
  font-weight:400;font-size:10px;letter-spacing:3px;text-align:center;line-height:21px}

.col-head{color:var(--red);font-weight:800;font-size:9px;padding-bottom:2px;border-bottom:.8px solid var(--rule);margin-bottom:5px}
.about{position:absolute;left:8px;top:206px;width:98px}
.about p{color:var(--grey);font-size:5.5px;line-height:1.5;margin-bottom:11px}
.col-rule{position:absolute;left:112px;top:206px;width:.8px;height:146px;background:var(--rule)}
.services{position:absolute;left:118px;top:206px;width:158px}
.services ul{list-style:none}
.services li{position:relative;padding-left:16px;color:var(--grey);font-size:5.5px;line-height:1.28;margin-bottom:3px}
.services li svg{position:absolute;left:1px;top:0;width:7px;height:7px}

.contact{position:absolute;left:0;top:355px;width:282px;height:45px}
.contact__labels,.contact__values{display:grid;grid-template-columns:62px 118px 42px 60px}
.contact__labels{height:9px;color:var(--red);font-weight:700;font-size:5.2px;line-height:9px}
.contact__values{height:21px;background:var(--red);color:#fff;font-size:5.1px;line-height:1.2;align-items:center}
.contact__labels span,.contact__values span{padding-left:8px;border-left:.8px solid var(--black)}
.contact__labels span:first-child,.contact__values span:first-child{border-left:none}
.licence{display:flex;gap:6px}
.contact__email{height:15px;background:var(--black);color:#fff;font-size:5.4px;text-align:center;line-height:15px}
.contact__email b{color:var(--red);font-weight:600}

.feature-photo{position:absolute;left:0;top:67px;width:115px;height:278px;background:linear-gradient(180deg,#3a3d40 0%,#55595c 45%,#b9bcbd 82%,#d4d6d6 100%)}
.values{position:absolute;left:115px;top:67px;width:162px;height:55px;background:var(--black);padding:4px 8px}
.values h3{color:var(--red);font-weight:700;font-size:8px;margin-bottom:2px}
.values li{list-style:none;color:#fff;font-size:5.1px;line-height:1.75}
.why{position:absolute;left:120px;top:128px;width:158px}
.why .col-head{font-size:8.4px;margin-bottom:5px}
.why h4{color:var(--ink);font-weight:700;font-size:6.3px;line-height:1.12;text-transform:uppercase;margin-bottom:1px}
.why p{color:var(--grey);font-size:5.3px;line-height:1.25;margin-bottom:5px}
</style>
</head>
<body>

<section class="sheet sheet--front">
  <div class="mission">Dedicate ourselves to providing world class service to anyone in need, based on honesty, communication and respect</div>
  <div class="brand"><div class="brand__name">BRIGHTWIRE</div><div class="brand__sub">PRO</div></div>

  <div class="photo-grid">
    <div class="ph-house" role="img" aria-label="Modern home exterior lit at dusk"></div>
    <div class="ph-kitchen-dark" role="img" aria-label="Dark kitchen with downlights"></div>
    <div class="ph-kitchen-grey" role="img" aria-label="Grey kitchen with pendant lights"></div>
    <div class="ph-kitchen-warm" role="img" aria-label="Kitchen bench with under-cabinet lighting"></div>
    <div class="ph-kitchen-white" role="img" aria-label="Bright white kitchen with pendants"></div>
    <div class="ph-kitchen-bright" role="img" aria-label="Open kitchen and dining area"></div>
    <div class="ph-garden" role="img" aria-label="Garden path lights at night"></div>
    <div class="ph-living" role="img" aria-label="Living room with warm lighting"></div>
  </div>

  <div class="title-band">Capability Statement</div>

  <div class="about">
    <h2 class="col-head">WHO WE ARE</h2>
    <p>BrightWire Pro is a growing Electrical maintenance company based in the Inner West.</p>
    <p>We are established on sound service principles with honesty, communication, and respect at the forefront of every team member.</p>
    <p>We strive for openness, trust, and accountability and we are in the business of providing solutions to help others. We see ourselves as an extension of your team.</p>
  </div>
  <div class="col-rule"></div>

  <div class="services">
    <h2 class="col-head">SERVICES WE PROVIDE</h2>
    <ul>
      <li><svg viewBox="0 0 10 10"><circle cx="5" cy="5" r="5" fill="#e1302a"/><rect x="2.5" y="4.2" width="5" height="1.6" fill="#fff"/></svg>24/7 Emergency service</li>
      <li><svg viewBox="0 0 10 10"><circle cx="5" cy="5" r="5" fill="#e1302a"/><rect x="2.5" y="4.2" width="5" height="1.6" fill="#fff"/></svg>Switchboard UPGRADE and REPAIRS</li>
      <li><svg viewBox="0 0 10 10"><circle cx="5" cy="5" r="5" fill="#e1302a"/><rect x="2.5" y="4.2" width="5" height="1.6" fill="#fff"/></svg>Light fitting installations</li>
      <li><svg viewBox="0 0 10 10"><circle cx="5" cy="5" r="5" fill="#e1302a"/><rect x="2.5" y="4.2" width="5" height="1.6" fill="#fff"/></svg>Powerpoint installations</li>
      <li><svg viewBox="0 0 10 10"><circle cx="5" cy="5" r="5" fill="#e1302a"/><rect x="2.5" y="4.2" width="5" height="1.6" fill="#fff"/></svg>Surge device installations</li>
      <li><svg viewBox="0 0 10 10"><circle cx="5" cy="5" r="5" fill="#e1302a"/><rect x="2.5" y="4.2" width="5" height="1.6" fill="#fff"/></svg>Testing and servicing electric hot water systems</li>
      <li><svg viewBox="0 0 10 10"><circle cx="5" cy="5" r="5" fill="#e1302a"/><rect x="2.5" y="4.2" width="5" height="1.6" fill="#fff"/></svg>Smoke Alarm installation with compliance certificate</li>
      <li><svg viewBox="0 0 10 10"><circle cx="5" cy="5" r="5" fill="#e1302a"/><rect x="2.5" y="4.2" width="5" height="1.6" fill="#fff"/></svg>Electric Vehicle charging stations</li>
      <li><svg viewBox="0 0 10 10"><circle cx="5" cy="5" r="5" fill="#e1302a"/><rect x="2.5" y="4.2" width="5" height="1.6" fill="#fff"/></svg>Ceiling and Exhaust fan installations with roof and wall venting</li>
      <li><svg viewBox="0 0 10 10"><circle cx="5" cy="5" r="5" fill="#e1302a"/><rect x="2.5" y="4.2" width="5" height="1.6" fill="#fff"/></svg>Appliance installations</li>
      <li><svg viewBox="0 0 10 10"><circle cx="5" cy="5" r="5" fill="#e1302a"/><rect x="2.5" y="4.2" width="5" height="1.6" fill="#fff"/></svg>Fault finding</li>
      <li><svg viewBox="0 0 10 10"><circle cx="5" cy="5" r="5" fill="#e1302a"/><rect x="2.5" y="4.2" width="5" height="1.6" fill="#fff"/></svg>TV, DATA and FREE TO AIR Aerial installations</li>
    </ul>
  </div>

  <div class="contact">
    <div class="contact__labels"><span>Mobile Phone</span><span>Electrical license number</span><span>ABN:</span><span>Public Liability</span></div>
    <div class="contact__values">
      <span>Daniel - 0400 123 456<br>Ben - 0400 987 654</span>
      <span class="licence"><span style="border:none;padding:0">BrightWire Pro Pty Ltd<br>-450003C</span><span style="border:none;padding:0">Daniel - 300001C<br>Ben - 400002C</span></span>
      <span>1234 5678 900</span>
      <span>$20,000,000</span>
    </div>
    <div class="contact__email"><b>Email:</b> Services@brightwirepro.com.au</div>
  </div>
</section>

<section class="sheet sheet--back">
  <div class="mission">Dedicate ourselves to providing world class service to anyone in need, based on honesty, communication and respect</div>
  <div class="brand"><div class="brand__name">BRIGHTWIRE</div><div class="brand__sub">PRO</div></div>

  <div class="feature-photo" role="img" aria-label="Crystal pendant chandelier in a modern stairwell with glass balustrade"></div>

  <div class="values">
    <h3>CORE VALUES</h3>
    <ul>
      <li>- SAFETY AND SECURITY IS PRIORITY</li>
      <li>- SUPPORT WHEN YOU NEED IT MOST</li>
      <li>- SERVICE WITH AN OVER-THE-TOP WOW</li>
      <li>- SATISFACTION WITH LOYALTY AND INTEGRITY</li>
    </ul>
  </div>

  <div class="why">
    <h2 class="col-head">WHY CHOOSE BRIGHTWIRE PRO</h2>
    <h4>Support when you need it most</h4>
    <p>BrightWire provides around the clock assistance, whether during normal business hours or emergencies we are focused on providing solutions for our clients.</p>
    <h4>Fast and responsive team with a direct contact</h4>
    <p>BrightWire treats every one of our clients as a VIP. We pride ourselves on being able to provide a quick turn around for all our jobs. We make the whole process smooth, from booking the job to attending and completion.</p>
    <h4>Satisfaction with loyalty and integrity</h4>
    <p>We value our transparency and communication skills to deliver an outstanding performance which reflects our happy customer base.</p>
    <h4>We provide courtesy calls</h4>
    <p>The appointment will be confirmed the day before and our technicians will call you half an hour in advance on approach to the job</p>
    <h4>Licensed and insured technicians</h4>
    <p>All our technicians are experts of their field, with the relevant equipment, knowledge and licenses to carry out our duties.</p>
  </div>

  <div class="contact">
    <div class="contact__labels"><span>Mobile Phone</span><span>Electrical license number</span><span>ABN:</span><span>Public Liability</span></div>
    <div class="contact__values">
      <span>Daniel - 0400 123 456<br>Ben - 0400 987 654</span>
      <span class="licence"><span style="border:none;padding:0">BrightWire Pro Pty Ltd<br>-450003C</span><span style="border:none;padding:0">Daniel - 300001C<br>Ben - 400002C</span></span>
      <span>1234 5678 900</span>
      <span>$20,000,000</span>
    </div>
    <div class="contact__email"><b>Email:</b> Services@brightwirepro.com.au</div>
  </div>
</section>

</body>
</html>
```